Eye-Catching, Direct Marketing Residential Painting Flyer!

I am run a residential painting business and am looking for a flyer to be designed to mailout to potential customers.
I want the copy/wording to be designed similar to this flyer.

It's important that the person reading the flyer gets the benefits we're promoting which is why I want the wording/copy to be almost identical to the flyer attached.

However, the structure will be different. The flyer will be a postcard thick, 5 x11.5.
Double sided.

The name of the company is Brightwall Coaters.

I would also like the prominent colour to either be light green or orange.

Target Market(s)

Home Owners between the age of 45-80.

Industry/Entity Type

Painting And Decorating

Font styles to use
Serif

Colors
f68d4d
faa54b
f78f20
f37122
9bcb3c
abd037
cadf82

Requirements
Must have
• Excellent Eye-Catching Design
• Benefits Visibly Promoted
• Action Taking Incentive- Call Now for FREE Window Cleaning and FREE Painting Estimate
Should not have
• Crowded wording

```html
<!DOCTYPE html>
<html lang="en">
<head>
<meta charset="UTF-8">
<title>Brightwall Coaters – Trifold Flyer</title>
<link rel="stylesheet" href="https://fonts.googleapis.com/css2?family=Open+Sans:wght@400;600;700;800&family=Noto+Serif:ital,wght@1,700&display=swap">
<style>
:root{
  --orange:#f78f20;
  --orange-deep:#f37122;
  --orange-soft:#faa54b;
  --green:#9bcb3c;
  --green-alt:#abd037;
  --green-pale:#cadf82;
  --red:#e8322a;
  --ink:#4a4a4a;
  --white:#ffffff;
  --stage:#e4e4e4;
  --sans:'Open Sans', Arial, sans-serif;
  --serif:'Noto Serif', Georgia, serif;
}
*{box-sizing:border-box;margin:0;padding:0}
html,body{width:1200px;height:2397px;overflow:hidden}
body{background:var(--stage);font-family:var(--sans);position:relative}
.row{position:absolute;left:0;width:1200px;height:799px}
.row--cover{top:0}
.row--outside{top:799px}
.row--inside{top:1598px}
.sheet{position:absolute;top:50px;height:700px;display:flex;box-shadow:0 14px 30px rgba(0,0,0,.22)}
.row--cover .sheet{left:430px}
.row--outside .sheet,.row--inside .sheet{left:90px}
.panel{position:relative;width:340px;height:700px;overflow:hidden;background:var(--white)}

/* cover */
.brand{position:absolute;top:0;left:0;right:0;height:110px;background:var(--white);display:flex;align-items:center;gap:14px;padding:0 26px}
.brand__dot{width:44px;height:44px;border-radius:50%;background:var(--orange)}
.brand__name{font-weight:700;font-size:18px;color:var(--orange);text-transform:uppercase;letter-spacing:.5px}
.cover__photo{position:absolute;top:110px;left:0;right:0;height:420px;background:linear-gradient(160deg,#8d8d84 0%,#6f7165 45%,#8c8f57 75%,#6d7a4a 100%)}
.cover__question{position:absolute;top:140px;left:24px;right:24px;color:var(--white);font-size:19px;line-height:1.35;text-align:center}
.cover__promise{position:absolute;top:270px;left:24px;right:24px;color:var(--white);font-weight:800;font-size:17px;line-height:1.35;text-align:center}
.cover__band{position:absolute;left:0;right:0;top:470px;height:170px}
.cover__band svg{position:absolute;inset:0}
.cover__tagline{position:absolute;left:20px;right:20px;top:545px;color:var(--white);font-size:20px;font-weight:600;text-transform:uppercase;text-align:center;line-height:1.25}
.cover__web{position:absolute;left:0;right:0;bottom:0;height:60px;background:var(--green);color:var(--white);font-weight:700;font-size:17px;display:flex;align-items:center;justify-content:center}
.cover__portrait{position:absolute;top:350px;right:28px;width:150px;height:150px;border-radius:50%;border:6px solid var(--white);background:radial-gradient(circle at 50% 40%,#e9e4dc,#b8b2a8)}

/* outside spread */
.wall-photo{position:absolute;top:0;left:0;width:680px;height:250px;background:linear-gradient(180deg,#f3efe8 0%,#e2d9c8 70%,#c9a66b 100%)}
.testimonials{position:absolute;top:210px;left:0;width:340px;height:490px;background:var(--orange);padding:110px 26px 0 26px}
.testimonials__icon{position:absolute;top:-50px;left:28px;width:110px;height:110px;border-radius:50%;border:5px solid var(--white);background:radial-gradient(circle,#f2f2f2,#c9c9c9)}
.quote{position:relative;padding-left:30px;margin-bottom:30px;color:var(--white);font-size:12.5px;line-height:1.5;font-style:italic}
.quote::before{content:"\201C";position:absolute;left:0;top:-8px;font-size:34px;font-weight:800;color:var(--green-pale);font-style:normal}
.quote__author{display:block;font-style:normal;font-weight:600;margin-top:4px}
.offers{position:absolute;top:250px;left:340px;width:340px;height:390px;padding:16px 26px 0}
.offer{border:2px dashed var(--orange);padding:8px 12px;text-align:center;font-size:12.5px;line-height:1.4;color:var(--ink);margin-bottom:12px}
.offer strong{color:var(--orange-deep);font-size:15px;font-weight:700}
.offer em{display:block;color:var(--orange);font-style:normal;font-weight:600}
.offers__cta{color:var(--red);font-weight:700;font-size:16.5px;line-height:1.3;text-align:center;margin-top:4px}
.phone-band{position:absolute;left:340px;bottom:0;width:340px;height:60px;background:var(--green);color:var(--white);font-weight:700;font-size:19px;display:flex;align-items:center;justify-content:center;gap:10px}

/* inside spread */
.scene{position:absolute;top:0;left:0;right:0;height:440px}
.scene--deck{background:linear-gradient(180deg,#8a8f7a 0%,#7b5a42 55%,#6a3f27 100%)}
.scene--garage{background:linear-gradient(180deg,#c9ccd0 0%,#e8e8e6 55%,#9a9fa3 100%)}
.scene--kitchen{background:linear-gradient(180deg,#efe7d8 0%,#9aa27a 50%,#c7a77e 100%)}
.inset{position:absolute;top:330px;left:115px;width:120px;height:120px;border-radius:50%;border:5px solid var(--white);z-index:2}
.inset--deck{background:linear-gradient(90deg,#a8835f,#6b4a33)}
.inset--door{background:linear-gradient(90deg,#dfe3e6,#7a5236)}
.inset--roller{background:radial-gradient(circle,#ffffff,#e4d7b0)}
.fix{position:absolute;top:440px;left:0;right:0;height:200px}
.fix svg{position:absolute;left:0;top:-22px;width:340px;height:222px}
.fix__text{position:relative;padding:12px 28px 0;color:var(--white);font-size:13.5px;line-height:1.4;text-align:center}
.fix__label{display:block;font-family:var(--serif);font-style:italic;font-weight:700;font-size:15px;margin-top:4px}
.floor{position:absolute;left:0;right:0;bottom:0;height:60px;background:linear-gradient(180deg,#7a5a40,#4b3322)}
</style>
</head>
<body>

<section class="row row--cover">
  <div class="sheet">
    <div class="panel cover">
      <div class="brand"><span class="brand__dot"></span><span class="brand__name">Brightwall Coaters</span></div>
      <div class="cover__photo" role="img" aria-label="Photo of open paint swatch fan decks in grey and green tones"></div>
      <p class="cover__question">Does your deck interior siding walls fence, windows, look faded dirty, out of date, are they chipping or peeling?</p>
      <p class="cover__promise">We make your home look CLEAN, FRESH &amp; Beautiful again!</p>
      <div class="cover__band"><svg viewBox="0 0 340 170" preserveAspectRatio="none"><path d="M0 40 Q170 -10 340 30 L340 170 L0 170Z" fill="var(--orange)"/></svg></div>
      <div class="cover__portrait" role="img" aria-label="Photo of a smiling painter holding a paint roller"></div>
      <p class="cover__tagline">Take control of how your home looks!</p>
      <div class="cover__web">www.brightwallcoaters.com</div>
    </div>
  </div>
</section>

<section class="row row--outside">
  <div class="sheet">
    <div class="panel"></div>
    <div class="panel"></div>
    <div class="panel cover">
      <div class="brand"><span class="brand__dot"></span><span class="brand__name">Brightwall Coaters</span></div>
      <div class="cover__photo" role="img" aria-label="Photo of open paint swatch fan decks in grey and green tones"></div>
      <p class="cover__question">Does your deck interior siding walls fence, windows, look faded dirty, out of date, are they chipping or peeling?</p>
      <p class="cover__promise">We make your home look CLEAN, FRESH &amp; Beautiful again!</p>
      <div class="cover__band"><svg viewBox="0 0 340 170" preserveAspectRatio="none"><path d="M0 40 Q170 -10 340 30 L340 170 L0 170Z" fill="var(--orange)"/></svg></div>
      <div class="cover__portrait" role="img" aria-label="Photo of a smiling painter holding a paint roller"></div>
      <p class="cover__tagline">Take control of how your home looks!</p>
      <div class="cover__web">www.brightwallcoaters.com</div>
    </div>
    <div class="wall-photo" role="img" aria-label="Photo of a white wall with green, yellow and red paint roller stripes above a wooden floor with paint tins"></div>
    <div class="testimonials">
      <div class="testimonials__icon" role="img" aria-label="Illustration of open paint cans with brushes"></div>
      <p class="quote">We couldn't be happier with the results. Clean, quick and friendly crew!<span class="quote__author">Maria &amp; Greg, Oakdale</span></p>
      <p class="quote">They refreshed our whole exterior and left the yard spotless. Highly recommend to any neighbour.<span class="quote__author">Tom R., Lakeview</span></p>
      <p class="quote">Fair price, on time and great attention to detail. Our kitchen looks brand new.<span class="quote__author">Janet &amp; Paul, Riverside</span></p>
    </div>
    <div class="offers">
      <div class="offer">If you are one of the<br><strong>first 12 exterior projects</strong><br>that book with us, you will receive a complimentary<em>window cleaning service</em></div>
      <div class="offer">If you are one of the<br><strong>first 12 interior projects</strong><br>that book with us, you will receive a complimentary<em>interior design consultation by a professional designer</em></div>
      <p class="offers__cta">Call Now for FREE Window Cleaning and FREE Painting Estimate</p>
    </div>
    <div class="phone-band">
      <svg width="20" height="20" viewBox="0 0 24 24"><path d="M6.6 10.8a15.1 15.1 0 0 0 6.6 6.6l2.2-2.2a1 1 0 0 1 1-.25 11.4 11.4 0 0 0 3.6.57 1 1 0 0 1 1 1V20a1 1 0 0 1-1 1A17 17 0 0 1 3 4a1 1 0 0 1 1-1h3.5a1 1 0 0 1 1 1c0 1.25.2 2.45.57 3.570a1 1 0 0 1-.25 1z" fill="var(--white)"/></svg>
      555-014-3075
    </div>
  </div>
</section>

<section class="row row--inside">
  <div class="sheet">
    <div class="panel">
      <div class="scene scene--deck" role="img" aria-label="Photo of a stone house patio with a wooden deck and lounge chairs"></div>
      <div class="inset inset--deck" role="img" aria-label="Close-up photo of freshly stained deck boards"></div>
      <div class="fix">
        <svg viewBox="0 0 340 222" preserveAspectRatio="none"><path d="M0 22 C60 0 110 30 170 14 C230 0 280 26 340 12 L340 222 L0 222Z" fill="var(--orange)"/></svg>
        <p class="fix__text"><span class="fix__label">Problem:</span>Your deck or fence is chipping or peeling, and looks old and faded.<span class="fix__label">Solution:</span>A fresh coat of stain will protect your investment and make it look clean, fresh and Beautiful again!</p>
      </div>
      <div class="floor" role="img" aria-label="Photo of dark wooden floorboards"></div>
    </div>
    <div class="panel">
      <div class="scene scene--garage" role="img" aria-label="Photo of a house exterior with white garage doors"></div>
      <div class="inset inset--door" role="img" aria-label="Close-up photo of a freshly painted front door"></div>
      <div class="fix">
        <svg viewBox="0 0 340 222" preserveAspectRatio="none"><path d="M0 16 C60 30 110 0 170 16 C230 30 280 2 340 18 L340 222 L0 222Z" fill="var(--orange-deep)"/></svg>
        <p class="fix__text"><span class="fix__label">Problem:</span>Your exterior windows, doors, garage doors, stucco, siding, soffits are chipping or peeling, and look old and faded.<span class="fix__label">Solution:</span>A fresh coat of paint will protect your investment and make it look clean, fresh and Beautiful again!</p>
      </div>
      <div class="floor" role="img" aria-label="Photo of dark wooden floorboards"></div>
    </div>
    <div class="panel">
      <div class="scene scene--kitchen" role="img" aria-label="Photo of a bright kitchen with green walls and white cabinets"></div>
      <div class="inset inset--roller" role="img" aria-label="Close-up photo of a hand rolling white paint on a wall"></div>
      <div class="fix">
        <svg viewBox="0 0 340 222" preserveAspectRatio="none"><path d="M0 14 C70 30 120 2 180 16 C240 30 290 4 340 16 L340 222 L0 222Z" fill="var(--green)"/></svg>
        <p class="fix__text"><span class="fix__label">Problem:</span>Is the colour in your interior basement, kitchen, bedrooms, and bathrooms walls, doors, and trim faded or out of date?<span class="fix__label">Solution:</span>A fresh coat of paint to make your interior look clean, fresh and Beautiful again!</p>
      </div>
      <div class="floor" role="img" aria-label="Photo of dark wooden floorboards"></div>
    </div>
  </div>
</section>

</body>
</html>
```